Brevant Business Card

I have a business that is called "Brevant Electrical Products LTD" My company deals with top of the range laptops and mobile phones that are exclusive. I need a business card that will be eye catching but not over complicated.

Target Market(s)

Adults aged 19 to 50
Upper middle class

Industry/Entity Type

Business

Requirements
Must have
• Company name/logo (file attached)
• It must have my contact information which is:

• Name: Dale Marwick

• Position: Managing Director 

• Business Address: 7 Hapton Row, London, W4 9QD

• Contact Number: 02085193604
• Mobile: 07814260537
• Email: info@brevant-goods.co.uk
Nice to have
• Simple and stylish
• Eye catching

```html
<!DOCTYPE html>
<html lang="en">
<head>
<meta charset="utf-8">
<title>Brevant Business Card</title>
<link rel="stylesheet" href="https://fonts.googleapis.com/css2?family=Didact+Gothic&family=Nunito+Sans:wght@800&display=swap">
<style>
  :root {
    --page: #ffffff;
    --card-top: #ffffff;
    --card-bottom: #7cfbec;
    --frame: #1d5f73;
    --ink: #1b5872;
    --navy: #223f8c;
    --brand: #44e4f2;
    --disc: #2f6b80;
    --disc-dark: #245a6d;
  }
  * { margin: 0; padding: 0; box-sizing: border-box; }
  html, body {
    width: 1178px; height: 1200px; overflow: hidden;
    background: var(--page);
  }
  .canvas { position: relative; width: 1178px; height: 1200px; }
  .card {
    position: absolute;
    width: 656px; height: 372px;
    border: 2px solid var(--frame);
    background: linear-gradient(to bottom, var(--card-top) 0%, var(--card-top) 25%, var(--card-bottom) 100%);
    overflow: hidden;
  }
  .card--front { left: 190px; top: 384px; }
  .card--back { left: 332px; top: 828px; }
  .disc {
    position: absolute;
    width: 220px; height: 220px; border-radius: 50%;
    background: radial-gradient(circle at 45% 40%, var(--disc) 0%, var(--disc-dark) 100%);
    box-shadow: 12px 12px 28px rgba(0, 0, 0, 0.35);
  }
  .card--front .disc { left: -12px; top: -8px; }
  .card--back .disc { left: 442px; top: -9px; }

  .brand-name {
    position: absolute; left: 0; right: 0; top: 78px;
    text-align: center;
    font-family: "Didact Gothic", sans-serif;
    font-size: 128px; line-height: 1;
    letter-spacing: 4px;
    color: var(--brand);
  }
  .brand-tagline {
    position: absolute; left: 0; right: 0; top: 218px;
    text-align: center;
    font-family: "Didact Gothic", sans-serif;
    font-size: 51px; line-height: 1;
    letter-spacing: 4px;
    color: var(--navy);
  }
  .address {
    position: absolute; left: 0; right: 0; top: 322px;
    text-align: center;
    font-family: "Didact Gothic", sans-serif;
    font-size: 17px;
    color: var(--ink);
  }

  .person-name {
    position: absolute; left: 39px; top: 50px;
    font-family: "Nunito Sans", sans-serif; font-weight: 800;
    font-size: 46px; line-height: 1;
    color: var(--ink);
  }
  .person-role {
    position: absolute; left: 195px; top: 106px;
    font-family: "Nunito Sans", sans-serif; font-weight: 800;
    font-size: 25px; line-height: 1;
    color: var(--ink);
  }
  .contact-list {
    position: absolute; left: 155px; top: 211px;
    list-style: none;
    font-size: 31px; line-height: 38px;
    color: var(--ink);
  }
  .contact-label {
    display: inline-block; width: 122px;
    font-family: "Nunito Sans", sans-serif; font-weight: 800;
  }
  .contact-value { font-family: "Didact Gothic", sans-serif; }
  .email {
    position: absolute; left: 0; right: 0; top: 309px;
    text-align: center;
    font-family: "Nunito Sans", sans-serif; font-weight: 800;
    font-size: 30px; line-height: 1;
    color: var(--ink);
  }
</style>
</head>
<body>
<main class="canvas">
  <section class="card card--front">
    <div class="disc" role="img" aria-label="Textured teal woven disc decoration"></div>
    <h1 class="brand-name">BREVANT</h1>
    <p class="brand-tagline">Electrical Products</p>
    <p class="address">7 Hapton Row, London W4 9QD</p>
  </section>

  <section class="card card--back">
    <div class="disc" role="img" aria-label="Textured teal woven disc decoration"></div>
    <h2 class="person-name">Dale Marwick</h2>
    <p class="person-role">Managing Director</p>
    <ul class="contact-list">
      <li><span class="contact-label">Phone:</span><span class="contact-value">0 208 519 3604</span></li>
      <li><span class="contact-label">Mobile:</span><span class="contact-value">0 781 426 0537</span></li>
    </ul>
    <p class="email">info@brevant-goods.co.uk</p>
  </section>
</main>
</body>
</html>
```